Business Card Re-Design

Consulting Company: To build a high performance organization, you need great leaders at all levels throughout your organization. The Northvale Talent Growth Studio engages, inspires, and educates current and future leaders to step beyond the ordinary and deliver exceptional results. This new breed of leaders will motivate your staff to leave the safety of complacency behind and come together to build an extraordinary organization. The current trend has been to ask our people to do more with fewer resources. People have been stepping up to the challenge, but more is required to ensure success with a new work paradigm. We work with your management team to build a successful strategy that will make your organization more effective. NTGS then supports your management team by providing a comprehensive set of proven services to empower your entire organization to successfully execute new strategies.Let NTGS help you optimize your organization’s individual and team performance today!

Target Market(s)

Federal, State and Local Government / Non profit

Industry/Entity Type

Management Consulting

Contact Information for Business Card

NTGS, inc (Northvale Talent Growth Studio) Optimizing Individual and Organizational Performance

Colors
fee18a
ec1f27
474747
fbf289

Requirements
Must have
• Professional and high quality feel

```html
<!DOCTYPE html>
<html lang="en">
<head>
<meta charset="utf-8">
<title>NTGS Business Card</title>
<link rel="stylesheet" href="https://fonts.googleapis.com/css2?family=Tinos:wght@400;700&display=swap">
<style>
  :root {
    --ink: #474747;
    --red: #ec1f27;
    --gold: #fee18a;
    --paper: #ffffff;
    --paper-shade: #f3f3f3;
    --band: #4a4a4a;
    --band-dark: #3a3a3a;
    --rule: #dcdcdc;
    --backdrop: #e9e6e1;
  }
  * { box-sizing: border-box; margin: 0; padding: 0; }
  html, body { width: 1200px; height: 1022px; overflow: hidden; }
  body {
    background: var(--backdrop);
    font-family: "Tinos", "Times New Roman", serif;
    color: var(--ink);
    position: relative;
  }
  .card {
    position: absolute;
    left: 170px;
    width: 860px;
    height: 470px;
    background: linear-gradient(160deg, var(--paper) 0%, var(--paper-shade) 100%);
    border-radius: 14px;
    overflow: hidden;
    box-shadow: 0 8px 24px rgba(0,0,0,.18);
  }
  .card--front { top: 28px; }
  .card--back { top: 524px; }

  .base-band {
    position: absolute; left: 0; right: 0; bottom: 0; height: 62px;
    background: linear-gradient(180deg, var(--band) 0%, var(--band-dark) 100%);
  }
  .base-rule {
    position: absolute; left: 0; right: 0; bottom: 74px; height: 5px;
    background: var(--red);
  }
  .corner-tab {
    position: absolute; left: 0; top: 40px; width: 16px; height: 62px;
    background: var(--red);
  }
  .person { position: absolute; left: 62px; top: 46px; }
  .person__name {
    font-weight: 700; font-size: 34px; letter-spacing: 1.5px;
    text-transform: uppercase; color: var(--ink);
  }
  .person__title {
    margin-top: 6px; font-size: 24px; letter-spacing: 1px;
    text-transform: uppercase; color: var(--red);
  }
  .divider {
    position: absolute; left: 62px; right: 62px; bottom: 210px;
    height: 1px; background: var(--rule);
  }
  .contact {
    position: absolute; left: 62px; bottom: 96px; list-style: none;
    font-size: 22px; color: var(--ink); line-height: 34px;
  }
  .contact li { display: flex; align-items: center; gap: 14px; }
  .contact svg { width: 18px; height: 18px; fill: none; stroke: var(--red); stroke-width: 2; }

  .brand { position: absolute; display: flex; align-items: center; gap: 18px; }
  .brand__mark { width: 26px; height: 26px; background: var(--red); }
  .brand__name { font-weight: 700; font-size: 80px; letter-spacing: 6px; color: var(--ink); line-height: 1; }
  .brand__line { font-size: 20px; color: var(--red); letter-spacing: .5px; margin-top: 10px; }
  .card--front .brand-block { position: absolute; right: 62px; top: 46px; text-align: right; }
  .card--front .brand { position: static; justify-content: flex-end; }

  .card--back .brand-block {
    position: absolute; left: 0; right: 0; top: 130px; text-align: center;
  }
  .card--back .brand { position: static; justify-content: center; }
  .card--back .brand__name { font-size: 110px; }
  .card--back .brand__line { font-size: 24px; margin-top: 16px; }
</style>
</head>
<body>
  <section class="card card--front" aria-label="Business card front">
    <div class="corner-tab"></div>
    <div class="person">
      <p class="person__name">Daniel R. Whitmore</p>
      <p class="person__title">President/CEO</p>
    </div>
    <div class="brand-block">
      <div class="brand">
        <span class="brand__mark"></span>
        <span class="brand__name">NTGS</span>
      </div>
      <p class="brand__line">Northvale Talent Growth Studio</p>
    </div>
    <div class="divider"></div>
    <ul class="contact">
      <li>
        <svg viewBox="0 0 20 20"><path d="M5 2l3 4-2 2c1 2 3 4 5 5l2-2 4 3-2 3C8 17 3 12 2 5z"/></svg>
        555-210-4837
      </li>
      <li>
        <svg viewBox="0 0 20 20"><rect x="2" y="4" width="16" height="12"/><path d="M2 4l8 7 8-7"/></svg>
        dwhitmore@ntgsinc.com
      </li>
      <li>
        <svg viewBox="0 0 20 20"><circle cx="10" cy="10" r="8"/><path d="M2 10h16M10 2c3 3 3 13 0 16M10 2c-3 3-3 13 0 16"/></svg>
        www.ntgsinc.com
      </li>
    </ul>
    <div class="base-rule"></div>
    <div class="base-band"></div>
  </section>

  <section class="card card--back" aria-label="Business card back">
    <div class="brand-block">
      <div class="brand">
        <span class="brand__mark"></span>
        <span class="brand__name">NTGS</span>
      </div>
      <p class="brand__line">Northvale Talent Growth Studio</p>
    </div>
    <div class="base-rule"></div>
    <div class="base-band"></div>
  </section>
</body>
</html>
```